Velmora Intergrated Marketing Stationary Design Contest

We require a very professional looking stationary set to include: letterhead, compliments slip and business cards (double sided bus cards).

Files should be supplied on either Illustrator or InDesign.

We are interested in perhaps encorporating a faint watermark with the letter q or the logo, but it isnt a pre-requisite

Target Market(s)

Business owners seeking professional marketing services

Industry/Entity Type

Marketing

Requirements
Must have
• Concurrent theme wiht business cards, letterhead and comp slip. Must be an editable document for future ammendment
Should not have
• No use of times new roman or similar fonts

```html
<!DOCTYPE html>
<html lang="en">
<head>
<meta charset="utf-8">
<title>Velmora Integrated Marketing – Stationery Set</title>
<link rel="stylesheet" href="https://fonts.googleapis.com/css2?family=Open+Sans:wght@300;400&family=Mrs+Saint+Delafield&display=swap">
<style>
  :root {
    --brand-orange: #f05a28;
    --band-red: #ec1c24;
    --band-orange: #f47b20;
    --band-yellow: #ffc700;
    --watermark: #fde3d8;
    --ink: #3a3a3a;
    --ink-soft: #6d6d6d;
    --paper: #ffffff;
    --frame: #9a9a9a;
  }
  * { box-sizing: border-box; margin: 0; padding: 0; }
  html, body { width: 960px; height: 1200px; overflow: hidden; background: var(--paper); }
  body { position: relative; font-family: "Open Sans", Arial, sans-serif; color: var(--ink); }

  .sheet {
    position: absolute; background: var(--paper); overflow: hidden;
    border: 1px solid var(--frame);
    box-shadow: 3px 3px 3px rgba(0,0,0,0.45);
  }
  .sheet::after {
    content: ""; position: absolute; inset: 3px; border: 1px solid #b5b5b5; pointer-events: none;
  }

  .watermark {
    position: absolute; border-radius: 50%;
    background: radial-gradient(circle at 55% 45%, var(--watermark) 0%, var(--watermark) 55%, rgba(253,227,216,0) 72%);
  }

  .brand { position: absolute; display: flex; align-items: center; gap: 6px; }
  .brand-dot { border-radius: 50%; background: var(--brand-orange); flex: none; }
  .brand-text { display: flex; flex-direction: column; line-height: 1; }
  .brand-name { font-weight: 300; color: var(--ink); letter-spacing: 0.12em; }
  .brand-tagline { font-weight: 300; color: var(--ink-soft); letter-spacing: 0.08em; margin-top: 2px; }

  .address { position: absolute; text-align: right; color: var(--ink); font-weight: 400; }

  .bands { position: absolute; left: 0; right: 0; }
  .band-yellow { background: var(--band-yellow); }
  .band-orange { background: var(--band-orange); }
  .band-red {
    background: var(--band-red); color: #fff; display: flex; justify-content: center; align-items: center;
    gap: 20px; font-size: 8.5px;
  }

  /* Letterhead */
  .letterhead { left: 56px; top: 74px; width: 502px; height: 708px; }
  .letterhead .watermark { left: -170px; top: 144px; width: 500px; height: 500px; }
  .letterhead .brand { right: 29px; top: 18px; }
  .letterhead .brand-dot { width: 24px; height: 24px; }
  .letterhead .brand-name { font-size: 17px; }
  .letterhead .brand-tagline { font-size: 5.5px; }
  .letterhead .address { right: 29px; top: 46px; font-size: 4.4px; line-height: 1.55; }
  .letterhead .bands { top: 659px; }
  .letterhead .band-yellow { height: 6px; }
  .letterhead .band-orange { height: 6px; }
  .letterhead .band-red { height: 21px; }

  /* Business card front */
  .card-front { left: 466px; top: 362px; width: 212px; height: 122px; }
  .card-front .brand { left: 27px; top: 11px; }
  .card-front .brand-dot { width: 40px; height: 40px; }
  .card-front .brand-name { font-size: 24px; }
  .card-front .brand-tagline { font-size: 8px; }
  .card-front .bands { top: 59px; }
  .card-front .band-yellow { height: 5px; }
  .card-front .band-orange { height: 5px; }
  .card-front .band-red { height: 35px; }

  /* Business card back */
  .card-back { left: 698px; top: 362px; width: 214px; height: 124px; border: none; }
  .card-back::after { display: none; }
  .card-back .watermark { left: -80px; top: 10px; width: 180px; height: 180px; }
  .card-back .bands-top { top: 0; }
  .card-back .bands-top .band-yellow { height: 5px; }
  .card-back .bands-top .band-orange { height: 6px; }
  .card-back .bands-bottom { bottom: 0; height: 19px; background: var(--band-yellow); }
  .signature { position: absolute; left: 10px; top: 14px; font-family: "Mrs Saint Delafield", cursive; font-size: 15px; color: #222; }
  .job-title { position: absolute; left: 11px; top: 31px; font-size: 3.8px; color: var(--ink-soft); }
  .card-back .address { right: 11px; top: 15px; font-size: 5.6px; line-height: 1.45; }
  .card-back .address .gap { height: 8px; }

  /* Compliments slip */
  .comp-slip { left: 323px; top: 851px; width: 520px; height: 261px; }
  .comp-slip .watermark { left: 290px; top: -40px; width: 300px; height: 300px; }
  .comp-slip .brand { left: 21px; top: 16px; }
  .comp-slip .brand-dot { width: 48px; height: 48px; }
  .comp-slip .brand-name { font-size: 30px; }
  .comp-slip .brand-tagline { font-size: 9.5px; }
  .comp-slip .address { right: 21px; top: 27px; font-size: 4.6px; line-height: 1.55; }
  .greeting {
    position: absolute; left: 0; right: 0; top: 110px; text-align: center;
    font-family: "Mrs Saint Delafield", cursive; font-size: 40px; color: #1f1f1f; padding-left: 75px;
  }
  .comp-slip .bands { top: 213px; }
  .comp-slip .band-yellow { height: 6px; }
  .comp-slip .band-orange { height: 6px; }
  .comp-slip .band-red { height: 21px; }
</style>
</head>
<body>

  <section class="sheet letterhead" aria-label="Letterhead">
    <div class="watermark" role="img" aria-label="Faint brand watermark"></div>
    <div class="brand">
      <span class="brand-dot"></span>
      <span class="brand-text">
        <span class="brand-name">velmora</span>
        <span class="brand-tagline">Integrated Marketing</span>
      </span>
    </div>
    <div class="address">
      Velmora Integrated Marketing<br>
      Harbour Offices, Mill Lane<br>
      Thornbury, North Ridings, TR7 4QX<br>
      Web www.velmoraim.co.uk<br>
      Email hello@velmoraim.co.uk<br>
      Tel 01632 960214<br>
      Fax 01632 960211
    </div>
    <div class="bands">
      <div class="band-yellow"></div>
      <div class="band-orange"></div>
      <div class="band-red">
        <span>Company registration 4815207</span>
        <span>Vat No 571 2048 36</span>
        <span>Trading as a division of Brindle Works Ltd</span>
      </div>
    </div>
  </section>

  <section class="sheet card-front" aria-label="Business card front">
    <div class="brand">
      <span class="brand-dot"></span>
      <span class="brand-text">
        <span class="brand-name">velmora</span>
        <span class="brand-tagline">Integrated Marketing</span>
      </span>
    </div>
    <div class="bands">
      <div class="band-yellow"></div>
      <div class="band-orange"></div>
      <div class="band-red"></div>
    </div>
  </section>

  <section class="sheet card-back" aria-label="Business card back">
    <div class="watermark" role="img" aria-label="Faint brand watermark"></div>
    <div class="bands bands-top">
      <div class="band-yellow"></div>
      <div class="band-orange"></div>
    </div>
    <div class="signature">Elliot Marsh</div>
    <div class="job-title">General Manager</div>
    <div class="address">
      Velmora Integrated Marketing<br>
      Harbour Offices<br>
      Mill Lane<br>
      Thornbury<br>
      North Ridings<br>
      TR7 4QX
      <div class="gap"></div>
      Web www.velmoraim.co.uk<br>
      Email elliot@velmoraim.co.uk<br>
      Tel 01632 960214<br>
      Fax 01632 960211
    </div>
    <div class="bands bands-bottom"></div>
  </section>

  <section class="sheet comp-slip" aria-label="Compliments slip">
    <div class="watermark" role="img" aria-label="Faint brand watermark"></div>
    <div class="brand">
      <span class="brand-dot"></span>
      <span class="brand-text">
        <span class="brand-name">velmora</span>
        <span class="brand-tagline">Integrated Marketing</span>
      </span>
    </div>
    <div class="address">
      Velmora Integrated Marketing<br>
      Harbour Offices, Mill Lane<br>
      Thornbury, North Ridings, TR7 4QX<br>
      Web www.velmoraim.co.uk<br>
      Email hello@velmoraim.co.uk<br>
      Tel 01632 960214<br>
      Fax 01632 960211
    </div>
    <p class="greeting">With Best Compliments</p>
    <div class="bands">
      <div class="band-yellow"></div>
      <div class="band-orange"></div>
      <div class="band-red">
        <span>Company registration 4815207</span>
        <span>Vat No 571 2048 36</span>
        <span>Trading as a division of Brindle Works Ltd</span>
      </div>
    </div>
  </section>

</body>
</html>
```